'TOLVANTA' NEW WINE LABEL DESIGN

I am looking for an exceptional and exciting design for a wine label called 'Tolvanta' meaning 'Lookout'. The design must feature the name 'Tolvanta', and the word 'Cabernet Sauvignon' in version 1 and 'Sauvignon Blanc' in version 2. It will also need the words 'Valle Central, Chile' at the bottom of the label as a prominent piece of information as well as the vintage 2017. Please produce the work in size 80mm x 100mm. Feel free to use colour in addition to black/white and ensue that the label is easy to read on a shelf placement.
Target Market(s)
SUPERMARKETS & WINE STORES
Requirements
Must have
- EASY TO READ, USE COLOURS LIKE GREEN FOR SAUVIGNON & RED FOR CABERNET SAUVIGNON
- FULL BOTTLE SHOT MUST BE IN PROVIDED DESIGNS. ALL BOTTLE TOPS SHOULD BE QUORLAN STYLE (SCREW TOP)
- PLEASE NOTE THAT LABEL INFORMATION MUSY BE EASY TO READ I.E. VINTAGE, PLACE OF ORGIN ALTHOUGH NOT THE MAIN CONTENT MUST STILL BE CLEAR.
Nice to have
- ARTISTIC REFERENCE LINK TO NAME & ANDES BUT NOT PICTURES OF MOUNTAINS
Should not have
- PICTURES OF GRAPES
- PICTURES OF VINEYARDS
- PICTURES OF MOUNTAINS

```html
<!DOCTYPE html>
<html lang="en">
<head>
<meta charset="utf-8">
<title>Tolvanta — Wine Labels</title>
<link rel="stylesheet" href="https://fonts.googleapis.com/css2?family=EB+Garamond:wght@400;500&family=Montserrat:wght@400;500&display=swap">
<style>
  :root {
    --page-bg: #ffffff;
    --label-paper: #f3f0e2;
    --ink-dark: #3a3a36;
    --blanc-name: #5f7a22;
    --blanc-art-light: #cfdc86;
    --blanc-art-mid: #a3b83e;
    --blanc-art-deep: #7d9428;
    --cab-name: #9a1d24;
    --cab-art-light: #e88074;
    --cab-art-mid: #d8433d;
    --cab-art-deep: #c22f2f;
  }
  * { margin: 0; padding: 0; box-sizing: border-box; }
  html, body {
    width: 1049px;
    height: 1200px;
    overflow: hidden;
    background: var(--page-bg);
  }
  .label-range {
    position: relative;
    width: 1049px;
    height: 1200px;
    display: flex;
    justify-content: center;
    align-items: center;
    gap: 60px;
  }
  .wine-label {
    position: relative;
    width: 440px;
    height: 550px;
    background: var(--label-paper);
    overflow: hidden;
    box-shadow: 0 0 0 1px rgba(0,0,0,0.06);
  }
  .wine-label__vintage {
    position: absolute;
    left: 24px;
    top: 26px;
    font-family: "Montserrat", sans-serif;
    font-size: 18px;
    letter-spacing: 0.12em;
    color: var(--ink-dark);
  }
  .wine-label__titles {
    position: absolute;
    right: 22px;
    top: 130px;
    text-align: right;
  }
  .wine-label__brand {
    font-family: "EB Garamond", serif;
    font-weight: 400;
    font-size: 35px;
    letter-spacing: 0.04em;
    line-height: 1;
  }
  .wine-label__varietal {
    margin-top: 6px;
    font-family: "EB Garamond", serif;
    font-weight: 400;
    font-size: 19px;
    letter-spacing: 0.06em;
    color: #2e2e2a;
    line-height: 1;
  }
  .wine-label__art {
    position: absolute;
    left: 0;
    right: 0;
    top: 205px;
    bottom: 62px;
  }
  .wine-label__origin {
    position: absolute;
    left: 0;
    right: 0;
    bottom: 0;
    height: 62px;
    display: flex;
    align-items: center;
    justify-content: center;
    font-family: "Montserrat", sans-serif;
    font-weight: 500;
    font-size: 16px;
    letter-spacing: 0.2em;
    text-transform: uppercase;
    color: var(--ink-dark);
    background: var(--label-paper);
  }
  .wine-label--blanc .wine-label__brand { color: var(--blanc-name); }
  .wine-label--blanc .wine-label__art {
    background: linear-gradient(180deg,
      rgba(163,184,62,0) 0%,
      var(--blanc-art-mid) 22%,
      var(--blanc-art-light) 58%,
      var(--blanc-art-deep) 100%);
  }
  .wine-label--cabernet .wine-label__brand { color: var(--cab-name); }
  .wine-label--cabernet .wine-label__art {
    background: linear-gradient(180deg,
      rgba(216,67,61,0) 0%,
      var(--cab-art-deep) 22%,
      var(--cab-art-mid) 60%,
      var(--cab-art-light) 100%);
  }
</style>
</head>
<body>
  <main class="label-range">
    <section class="wine-label wine-label--blanc">
      <p class="wine-label__vintage">2017</p>
      <div class="wine-label__titles">
        <h1 class="wine-label__brand">TOLVANTA</h1>
        <h2 class="wine-label__varietal">SAUVIGNON BLANC</h2>
      </div>
      <div class="wine-label__art" role="img" aria-label="Green watercolour ridges layered with fine white contour lines"></div>
      <p class="wine-label__origin">Valle Central, Chile</p>
    </section>

    <section class="wine-label wine-label--cabernet">
      <p class="wine-label__vintage">2017</p>
      <div class="wine-label__titles">
        <h1 class="wine-label__brand">TOLVANTA</h1>
        <h2 class="wine-label__varietal">CABERNET SAUVIGNON</h2>
      </div>
      <div class="wine-label__art" role="img" aria-label="Red watercolour ridges layered with fine white contour lines"></div>
      <p class="wine-label__origin">Valle Central, Chile</p>
    </section>
  </main>
</body>
</html>
```